We need to a website for a contact center that provides answering services by voice and chat.

A similar website in terms of design is the following site:
http://www.brindlecallhub.net/

The colors and look and feel should be different and creative but the structure should be similar to the above mentioned website.

Attached is the text file.

The design should communicate professionalism and friendly customer service oriented company. The visitor to the site must have a feel that "this company looks professional and they will take care of my client."

I am looking for design only, but if the designer will also do the coding, it will be an advantage.

Target Market(s)

Our target market are lawyers and doctors who require someone to answer their clients calls 24/7.

Industry/Entity Type

It Company

Requirements
Nice to have
• Since the company is based in Dubai, the website should reflect the Middle East people not pure European or pure Asians. A mixture of nationalities is fine to be visible in the pictures but it must include at least an arab or middle eastern person.
Should not have
• No old style, Times Roman font, do not include illustrations or cartoon graphics or pictures that are very common or widely used.

```html
<!DOCTYPE html>
<html lang="en">
<head>
<meta charset="utf-8">
<title>Cedar Voice – 24/7 Call Center</title>
<link href="https://fonts.googleapis.com/css2?family=Open+Sans:wght@400;600;700&display=swap" rel="stylesheet">
<style>
:root{
  --backdrop:#3f7d95;
  --backdrop-dark:#2a5a6e;
  --brand:#0d6a9a;
  --brand-dark:#0a5680;
  --nav-top:#1a86bd;
  --nav-bottom:#0b5f8c;
  --accent:#b72b3b;
  --accent-line:#d8545f;
  --panel:#efefef;
  --text:#555;
  --white:#fff;
}
*{box-sizing:border-box;margin:0;padding:0}
html,body{width:1200px;height:1176px;overflow:hidden}
body{
  font-family:"Open Sans",Arial,sans-serif;
  background:radial-gradient(ellipse at center,var(--backdrop) 0%,var(--backdrop-dark) 100%);
  position:relative;color:var(--text);
}
.page{
  position:absolute;left:156px;top:25px;width:880px;height:1125px;
  background:var(--white);border-radius:8px;overflow:hidden;
  box-shadow:0 0 30px rgba(0,0,0,.35);
}
.abs{position:absolute}
/* header */
.logo{left:25px;top:30px;font-size:33px;font-weight:700;color:var(--brand);letter-spacing:-.3px;line-height:1.1}
.tagline{left:48px;top:68px;font-size:17px;color:var(--brand);line-height:1.2}
.client-login{right:30px;top:18px;font-size:13px;color:var(--brand);text-decoration:underline}
.call-note{right:30px;top:54px;font-size:13px;color:#666}
.call-phone{right:30px;top:72px;font-size:22px;font-weight:600;color:var(--brand)}
/* nav */
.nav{
  left:0;top:111px;width:880px;height:50px;
  background:linear-gradient(var(--nav-top),var(--nav-bottom));
  display:flex;justify-content:space-between;align-items:center;padding:0 32px 0 25px;
}
.nav a{color:var(--white);font-size:13px;text-decoration:none;text-transform:uppercase}
.nav a.current{text-decoration:underline}
/* hero */
.hero{left:0;top:161px;width:880px;height:347px;overflow:hidden;background:#9fb6c8}
.hero svg.bg{position:absolute;left:0;top:0}
.hero-title{left:56px;top:88px;font-size:32px;color:var(--brand-dark)}
.hero-lead{left:54px;top:136px;width:420px;font-size:21px;line-height:28px;font-weight:600;color:var(--white);text-shadow:0 1px 3px rgba(0,0,0,.45)}
.cta{left:54px;top:216px;width:184px;height:49px;background:linear-gradient(#136fa3,var(--brand-dark));color:var(--white);font-size:20px;display:flex;align-items:center;justify-content:center;border-radius:2px}
.hero-photo{left:495px;top:28px;width:385px;height:319px;background:linear-gradient(180deg,#c7a29a 0%,#8a6a64 35%,#2b2b31 75%,#1e1e22 100%);border-radius:120px 120px 0 0}
/* sidebar */
.side-box{left:0;width:239px;height:81px;background:var(--panel);border-top:3px solid var(--accent-line)}
.side-box svg{position:absolute;left:20px;top:18px}
.side-box .label{position:absolute;left:82px;top:17px;font-size:15px;color:var(--brand)}
.side-box .more{position:absolute;left:82px;top:45px;font-size:11.5px;color:#333}
.side-head{left:0;width:239px;height:40px;background:var(--accent);color:var(--white);font-size:15px;padding:0 19px;display:flex;align-items:center}
.side-head b{font-weight:700;margin-right:4px}
.side-body{left:0;width:239px;background:var(--panel)}
.email{position:absolute;left:19px;top:10px;width:175px;height:31px;border:1px solid #ddd;background:var(--white);font-size:12px;color:#777;padding:7px 8px}
.go{position:absolute;left:200px;top:10px;width:33px;height:31px;background:#444;color:var(--white);font-size:12px;font-weight:600;display:flex;align-items:center;justify-content:center}
.social{position:absolute;top:10px;width:29px;height:29px;border-radius:4px;border:2px solid #cfd9e0}
/* main */
.main{left:264px;top:540px;width:600px;font-size:12px;line-height:17.7px;color:var(--text)}
.main h2{font-size:19px;font-weight:400;color:var(--brand);margin-bottom:8px;line-height:1.2}
.main p{margin-bottom:0}
.main ol{list-style:none;margin-bottom:18px}
.main .gap{margin-top:18px}
.main .closing{margin-top:18px;font-weight:600;color:#666}
.main .closing span{font-size:15px;font-weight:700;color:var(--brand)}
/* footer */
.footer{left:0;top:1063px;width:880px;height:62px;background:var(--brand-dark);border-top:3px solid #1e86bd;color:var(--white);font-size:12.5px;display:flex;align-items:center;padding:0 32px}
</style>
</head>
<body>
<div class="page">
  <header>
    <div class="abs logo">CEDAR VOICE</div>
    <div class="abs tagline">Company tagline goes here</div>
    <div class="abs client-login">Client Login</div>
    <div class="abs call-note">Please call Cedar Voice 24/7 at</div>
    <div class="abs call-phone">+9714-555-0188</div>
  </header>

  <nav class="abs nav">
    <a class="current">Home</a><a>About Us</a><a>Our Services</a><a>Our Methodology</a><a>How It Works</a><a>Pricing</a><a>FAQ</a><a>Contact Us</a>
  </nav>

  <section class="abs hero">
    <svg class="bg" width="880" height="347" viewBox="0 0 880 347">
      <defs>
        <linearGradient id="heroSky" x1="0" y1="0" x2="1" y2="1">
          <stop offset="0" stop-color="#c3d2de"/><stop offset="1" stop-color="#7e9bb4"/>
        </linearGradient>
      </defs>
      <rect width="880" height="347" fill="url(#heroSky)"/>
      <polygon points="0,60 170,0 0,0" fill="#d6e1ea" opacity=".7"/>
      <polygon points="0,347 880,150 880,347" fill="#8aa6bd" opacity=".7"/>
      <polygon points="0,347 880,230 880,347" fill="#7795ae" opacity=".6"/>
      <path d="M700,160 C780,110 840,60 880,0 L880,40 C840,100 790,140 700,160Z" fill="#e3ebf1" opacity=".5"/>
    </svg>
    <div class="abs hero-photo" role="img" aria-label="Smiling Middle Eastern man in a red and white keffiyeh and dark thobe"></div>
    <div class="abs hero-title">Welcome to our site</div>
    <div class="abs hero-lead">Cedar Voice is a24/7 call center and live answering service centre</div>
    <div class="abs cta">Get Started &gt;&gt;</div>
  </section>

  <aside>
    <div class="abs side-box" style="top:542px">
      <svg width="38" height="46" viewBox="0 0 38 46" fill="none" stroke="#0d6a9a" stroke-width="4">
        <rect x="3" y="7" width="32" height="37" rx="3"/><rect x="12" y="2" width="14" height="8" rx="2" fill="#0d6a9a"/>
        <line x1="11" y1="20" x2="27" y2="20"/><line x1="11" y1="28" x2="27" y2="28"/><line x1="11" y1="36" x2="27" y2="36"/>
      </svg>
      <div class="label">Request for Pricing</div><div class="more">CLICK HERE &#9655;</div>
    </div>
    <div class="abs side-box" style="top:637px">
      <svg width="38" height="46" viewBox="0 0 38 46" fill="#0d6a9a">
        <circle cx="19" cy="11" r="10"/><path d="M2,44 L2,32 Q2,24 12,24 L26,24 Q36,24 36,32 L36,44Z"/>
        <path d="M17,24 L21,24 L22,38 L19,42 L16,38Z" fill="#efefef"/>
      </svg>
      <div class="label">Online Signup</div><div class="more">CLICK HERE &#9655;</div>
    </div>
    <div class="abs side-box" style="top:733px">
      <svg width="44" height="46" viewBox="0 0 44 46" fill="none" stroke="#0d6a9a" stroke-width="3">
        <circle cx="22" cy="23" r="20"/>
        <path d="M15,13 L20,13 L21,19 L18,21 Q20,27 25,30 L27,27 L32,29 L32,34 Q26,36 19,30 Q13,23 15,13Z" fill="#0d6a9a" stroke="none"/>
      </svg>
      <div class="label">Contact Us</div><div class="more">CLICK HERE &#9655;</div>
    </div>

    <div class="abs side-head" style="top:830px"><b>Sign up</b> for Free Newsletter</div>
    <div class="abs side-body" style="top:870px;height:47px">
      <div class="email">Your Email id</div><div class="go">Go</div>
    </div>

    <div class="abs side-head" style="top:936px"><b>Follow Us</b></div>
    <div class="abs side-body" style="top:976px;height:47px">
      <div class="social" style="left:21px;background:#5a86b5" aria-label="Social link"></div>
      <div class="social" style="left:62px;background:#6fb7e0" aria-label="Social link"></div>
      <div class="social" style="left:103px;background:#f3c44a" aria-label="Feed link"></div>
      <div class="social" style="left:144px;background:#b6dde8" aria-label="Video link"></div>
    </div>
  </aside>

  <main class="abs main">
    <h2>24/7 Call Center and Live Answering Service</h2>
    <p>Cedar Voice is a24/7 call center and live answering service, we provide customized solutions for small, medium, and large organizations. Our customized solutions help our clients get the maximum return on their investment by capturing more leads and projecting a professional image to their customers, in addition tohuge savings on overhead and labor costs.</p>
    <h2 style="margin-top:24px">10 Ways Your Company Can Benefit</h2>
    <ol>
      <li>1.&nbsp; Capture more business &amp; increase profits.</li>
      <li>2.&nbsp; Save thousands on labor costs.</li>
      <li>3.&nbsp; Improve your company's "phone image".</li>
      <li>4.&nbsp; Streamline your call flow.</li>
      <li>5.&nbsp; Conduct business 24/7 without the overhead.</li>
      <li>6.&nbsp; Take advantage of a turn-key, streamlined solution.</li>
      <li>7.&nbsp; Respond instantaneously to clients and prospects.</li>
      <li>8.&nbsp; Cedar Voice uses the most reliable equipment in the industry.</li>
      <li>9.&nbsp; Cedar Voice selects the right people with the best voices.</li>
      <li>10.&nbsp; Cedar Voice over-staffs receptionists to minimize hold times.</li>
    </ol>
    <p>At Cedar Voice, we customize our services to each client's specific needs. We do not provide a "one size fits all" solutions. We take pride in developing solutions to fit the specific requirements of our clients' individual situation and needs.</p>
    <p>We employ the right people with the best voices and over-staff our team of live receptionists to minimize hold times. Our team of experts has experience spanning decades and cutting across industries to provide our customers with the right solution for their niche area of operation.</p>
    <p class="closing">For more information or to speak with an account specialist, please call Cedar Voice at <span>+ 9714-555-0188!</span></p>
  </main>

  <footer class="abs footer">Copyright@2013, Company Name</footer>
</div>
</body>
</html>
```